College audience knows my web site is bad. HELP Escape Room needs makeover

New escape room in college town needs web site to impress.
Need you to make my sad attempt at WIX better
Black silver vivid yellow. I have logo as starting point. Prefer something I can update. I have site that I made as example but I need more professional work.
Possible future design work. Thanks.

Target Market(s)

Younger. Games

Industry/Entity Type

College

Number of Pages Required

3 page

Font styles to use
Sans Serif

Colors
000000
fbed22
eaeaea
cbcbcb

Requirements
Must have
• Logo I just purchsed through plume orchard. Black silver vivid yellow .
Nice to have
• Photo gallery where I can add photos
• Contact page

```html
<!DOCTYPE html>
<html lang="en">
<head>
<meta charset="utf-8">
<title>The Lock Hall – Escape Rooms</title>
<link rel="stylesheet" href="https://fonts.googleapis.com/css2?family=Lato:wght@400;700&family=Chakra+Petch:wght@400;500&display=swap">
<style>
:root{
  --black:#000000;
  --yellow:#fbed22;
  --light:#eaeaea;
  --silver:#cbcbcb;
  --charcoal:#2e2e2e;
  --footer:#333333;
  --btn:#3a3a3a;
  --text-dark:#4a4a4a;
}
*{box-sizing:border-box;margin:0;padding:0}
html,body{width:1200px;height:2350px;overflow:hidden}
body{position:relative;font-family:'Lato',sans-serif;background:var(--light);color:#fff}
.abs{position:absolute}

/* header */
.top-strip{left:0;top:0;width:1200px;height:52px;background:var(--charcoal)}
.nav-strip{left:0;top:52px;width:1200px;height:66px;background:var(--black)}
.brand-box{left:81px;top:0;width:218px;height:168px;background:var(--black);border:2px solid #3c3c3c;border-top:none;display:flex;align-items:center;justify-content:center;z-index:3}
.brand-name{font-family:'Lato',sans-serif;font-weight:700;font-size:27px;color:var(--silver);letter-spacing:1px;text-transform:uppercase;text-align:center;line-height:1.15}
.contact-item{top:14px;display:flex;align-items:center;gap:12px;font-size:16px;color:#fff}
.icon-box{width:28px;height:26px;background:var(--yellow);display:flex;align-items:center;justify-content:center}
.book-top{left:991px;top:10px;width:128px;height:32px;background:var(--yellow);color:var(--black);font-size:16px;display:flex;align-items:center;justify-content:center;gap:8px}
.nav-link{top:74px;font-size:16px;color:var(--yellow);text-transform:uppercase}
.nav-active{left:518px;top:111px;width:62px;height:4px;background:var(--yellow)}

/* hero */
.hero{left:0;top:118px;width:1200px;height:559px;background:radial-gradient(ellipse at 55% 45%,#6c6c6c 0%,#3b3b3b 45%,#161616 100%)}
.hero-title{left:130px;top:306px;font-size:38px;font-weight:400;color:#fff;letter-spacing:.5px}
.hero-rule{left:130px;top:362px;width:372px;height:1px;background:#bdbdbd}
.hero-sub{left:130px;top:372px;font-size:21px;color:#fff}
.hero-btn{left:131px;top:412px;width:151px;height:44px;background:#5a5a5a;color:#fff;font-size:17px;display:flex;align-items:center;justify-content:center}
.arrow{top:365px}

/* welcome */
.welcome{left:0;top:677px;width:1200px;height:326px;background:var(--light);overflow:hidden}
.bar{position:absolute;top:0;height:326px;background:#d9d9d9}
.welcome-title{left:0;top:725px;width:1200px;text-align:center;font-family:'Chakra Petch',sans-serif;font-size:34px;color:#222}
.welcome-title b{font-family:'Lato',sans-serif;font-weight:700;color:#555;text-transform:uppercase;font-size:30px}
.welcome-rule{left:388px;top:780px;width:424px;height:2px;background:#222}
.welcome-copy{left:80px;top:810px;width:1040px;text-align:center;font-size:14.5px;line-height:24px;color:var(--text-dark)}
.dark-btn{left:525px;top:901px;width:150px;height:41px;background:var(--btn);color:#fff;font-size:16px;font-weight:700;display:flex;align-items:center;justify-content:center;border-radius:2px}

/* services */
.services{left:0;top:1003px;width:1200px;height:670px;background:radial-gradient(ellipse at 60% 40%,#3a3428 0%,#1a1813 55%,#070706 100%)}
.svc-label{font-size:17px;font-weight:700;color:#fff}
.svc-desc{font-size:13.5px;line-height:17px;color:#e6e6e6;width:270px}
.svc-active .svc-label,.svc-active .svc-desc{color:var(--yellow)}
.right{text-align:right}

/* gallery */
.gallery{left:0;top:1673px;width:1200px;height:387px;background:var(--light)}
.gallery-title{left:0;top:1722px;width:1200px;text-align:center;font-family:'Chakra Petch',sans-serif;font-size:34px;color:#222}
.gallery-rule{left:555px;top:1776px;width:90px;height:2px;background:#222}
.photo{top:1805px;width:297px;height:166px;box-shadow:3px 4px 6px rgba(0,0,0,.45)}
.caption{top:1987px;width:297px;text-align:center;font-size:14px;font-weight:700;color:#222}

/* footer */
.footer{left:0;top:2060px;width:1200px;height:243px;background:var(--footer)}
.foot-head{top:2112px;font-size:19px;color:var(--yellow)}
.foot-list{left:81px;top:2146px;list-style:none;font-size:13px;line-height:25px;color:#fff}
.foot-list li::before{content:"›";margin-right:9px;color:#ccc}
.foot-sep{top:2116px;width:1px;height:145px;background:#555}
.foot-row{display:flex;align-items:flex-start;gap:12px;font-size:13px;line-height:18px;color:#fff}
.map{left:487px;top:2117px;width:232px;height:143px;background:linear-gradient(135deg,#efe9d8,#e4dcc4 55%,#f0e48a)}
.social-dot{width:26px;height:26px;border-radius:50%;background:#fff}
.foot-brand{left:930px;top:2150px;width:200px;text-align:center;font-weight:700;font-size:30px;color:#8a8a8a;text-transform:uppercase;line-height:1.15}
.copyright{left:0;top:2303px;width:1200px;height:47px;background:var(--black);font-size:13px;color:#ddd;display:flex;align-items:center;justify-content:center}
</style>
</head>
<body>

<!-- header -->
<div class="abs top-strip"></div>
<div class="abs nav-strip"></div>
<div class="abs brand-box"><span class="brand-name">The Lock<br>Hall</span></div>

<div class="abs contact-item" style="left:528px">
  <span class="icon-box"><svg width="18" height="13" viewBox="0 0 18 13"><rect x="0.5" y="0.5" width="17" height="12" fill="#000"/><path d="M1 1l8 6 8-6" stroke="#fbed22" stroke-width="1.5" fill="none"/></svg></span>
  info@thelockhall.com
</div>
<div class="abs contact-item" style="left:796px">
  <span class="icon-box"><svg width="16" height="16" viewBox="0 0 24 24"><path d="M6.6 10.8a15 15 0 0 0 6.6 6.6l2.2-2.2a1 1 0 0 1 1-.25 11.4 11.4 0 0 0 3.6.57 1 1 0 0 1 1 1V20a1 1 0 0 1-1 1A17 17 0 0 1 3 4a1 1 0 0 1 1-1h3.5a1 1 0 0 1 1 1c0 1.25.2 2.45.57 3.57a1 1 0 0 1-.25 1z" fill="#000"/></svg></span>
  (555) 014-2290
</div>
<div class="abs book-top">
  <svg width="16" height="16" viewBox="0 0 24 24"><path d="M2 10h4v12H2zM8 22h10a2 2 0 0 0 2-1.6l1.8-8A2 2 0 0 0 20 10h-6l1-5a2 2 0 0 0-3.6-1.4L8 9z" fill="#000"/></svg>
  BOOK NOW
</div>

<nav>
  <span class="abs nav-link" style="left:528px">Home</span>
  <span class="abs nav-link" style="left:631px">About Us</span>
  <span class="abs nav-link" style="left:768px">Services</span>
  <span class="abs nav-link" style="left:899px">Gallery</span>
  <span class="abs nav-link" style="left:1025px">Contact Us</span>
</nav>
<div class="abs nav-active"></div>

<!-- hero -->
<section class="abs hero" role="img" aria-label="Black and white photograph of an abandoned, weathered room with open doorways and sunlight across the floor"></section>
<h1 class="abs hero-title">THE LOCK HALL</h1>
<div class="abs hero-rule"></div>
<p class="abs hero-sub">Opening March 17, 2016</p>
<a class="abs hero-btn">BOOK NOW</a>
<svg class="abs arrow" style="left:35px" width="38" height="68" viewBox="0 0 38 68"><path d="M36 2L3 34l33 32" stroke="#bbb" stroke-width="2" fill="none"/></svg>
<svg class="abs arrow" style="left:1127px" width="38" height="68" viewBox="0 0 38 68"><path d="M2 2l33 32L2 66" stroke="#bbb" stroke-width="2" fill="none"/></svg>

<!-- welcome -->
<section class="abs welcome">
  <div class="bar" style="left:0;width:80px"></div>
  <div class="bar" style="left:148px;width:46px"></div>
  <div class="bar" style="left:258px;width:40px;opacity:.7"></div>
  <div class="bar" style="left:420px;width:30px;opacity:.6"></div>
  <div class="bar" style="left:750px;width:30px;opacity:.6"></div>
  <div class="bar" style="left:900px;width:42px;opacity:.7"></div>
  <div class="bar" style="left:1010px;width:46px"></div>
  <div class="bar" style="left:1120px;width:80px"></div>
</section>
<h2 class="abs welcome-title">Welcome To <b>The Lock Hall</b></h2>
<div class="abs welcome-rule"></div>
<p class="abs welcome-copy">Lorem ipsum dolor sit amet, consectetuer adipiscing elit, sed diam nonummy nibh euismod tincidunt ut laoreet dolore magna aliquam erat volutpat. Duis autem vel eum iriure dolor in hendrerit in vulputate velit esse molestie consequat, vel illum dolore eu feugiat nulla facilisis at vero eros et accumsan et iusto odio dignissim qui blandit praesent luptatum zzril delenit augue duis dolore te feugait nulla facilisi.</p>
<a class="abs dark-btn">REED MORE</a>

<!-- services -->
<section class="abs services" role="img" aria-label="Dim photograph of a dark, abandoned corridor used as the background for the services"></section>
<svg class="abs" style="left:0;top:1003px" width="1200" height="670" viewBox="0 1003 1200 670">
  <g stroke="#9a9a9a" stroke-width="1.2" fill="none">
    <path d="M640 1139L940 1077"/><path d="M787 1275L840 1300H985"/>
    <path d="M790 1458L895 1528H1030"/><path d="M560 1536L475 1566H295"/>
    <path d="M390 1400L360 1396H182"/><path d="M396 1218L378 1211H185"/>
  </g>
  <g stroke="#ddd" stroke-width="1.5" stroke-dasharray="2 5" fill="none">
    <path d="M600 1213V1265M600 1415V1465M500 1270L535 1300M700 1270L665 1300M500 1410L535 1380M700 1410L665 1380"/>
  </g>
  <g fill="#fff"><circle cx="940" cy="1077" r="4"/><circle cx="985" cy="1300" r="4"/><circle cx="1030" cy="1528" r="4"/><circle cx="295" cy="1566" r="4"/><circle cx="182" cy="1396" r="4"/><circle cx="185" cy="1211" r="4"/></g>
  <g fill="#fff" stroke="#cfcfcf" stroke-width="5">
    <circle cx="599" cy="1155" r="56"/><circle cx="757" cy="1246" r="56"/>
    <circle cx="760" cy="1429" r="56"/><circle cx="599" cy="1523" r="56"/>
    <circle cx="440" cy="1429" r="56"/>
  </g>
  <circle cx="440" cy="1246" r="56" fill="#fbed22" stroke="#cfcfcf" stroke-width="5"/>
  <circle cx="600" cy="1340" r="74" fill="#000" stroke="#fff" stroke-width="7"/>
  <text x="600" y="1336" text-anchor="middle" font-family="Lato, sans-serif" font-weight="700" font-size="17" fill="#cbcbcb">THE LOCK</text>
  <text x="600" y="1358" text-anchor="middle" font-family="Lato, sans-serif" font-weight="700" font-size="17" fill="#cbcbcb">HALL</text>
  <!-- team -->
  <g fill="#111"><circle cx="599" cy="1141" r="8"/><path d="M584 1170a15 13 0 0 1 30 0z"/><circle cx="582" cy="1146" r="6"/><path d="M570 1168a12 11 0 0 1 22-4v4z"/><circle cx="616" cy="1146" r="6"/><path d="M606 1164a12 11 0 0 1 22 4h-22z"/></g>
  <!-- date night -->
  <g fill="#111"><circle cx="741" cy="1231" r="6"/><circle cx="773" cy="1231" r="6"/><rect x="735" y="1239" width="10" height="16"/><rect x="769" y="1239" width="10" height="16"/><rect x="746" y="1243" width="22" height="4"/><rect x="755" y="1247" width="4" height="18"/><rect x="733" y="1255" width="4" height="12"/><rect x="777" y="1255" width="4" height="12"/></g>
  <!-- parties -->
  <g fill="#111"><circle cx="760" cy="1412" r="7"/><path d="M752 1422h16l-3 24h-10z"/><path d="M740 1408l12 16-3 2-12-15zM780 1408l-12 16 3 2 12-15z"/><circle cx="742" cy="1424" r="5"/><circle cx="778" cy="1424" r="5"/><path d="M736 1432h12v14h-12zM772 1432h12v14h-12z"/></g>
  <!-- mysteries -->
  <g fill="none" stroke="#111" stroke-width="5"><circle cx="594" cy="1518" r="15"/><path d="M605 1529l13 13"/></g>
  <g fill="#111"><circle cx="594" cy="1513" r="5"/><path d="M584 1527a10 8 0 0 1 20 0z"/></g>
  <!-- riddles -->
  <path d="M424 1407h32v38h-10l-6 8-6-8h-10z" fill="#111"/>
  <text x="440" y="1438" text-anchor="middle" font-family="Lato, sans-serif" font-weight="700" font-size="26" fill="#fff">?</text>
  <!-- puzzles -->
  <g fill="#111"><rect x="422" y="1230" width="16" height="16"/><circle cx="438" cy="1238" r="5"/><rect x="442" y="1246" width="16" height="16"/><circle cx="450" cy="1246" r="5"/><rect x="420" y="1250" width="16" height="14"/></g>
</svg>

<div class="abs" style="left:807px;top:1067px;width:270px"><div class="svc-label right">Team Building</div><div class="svc-desc right" style="margin-top:6px">Lorem ipsum dolor sit amet, consectetuer adipiscing elit</div></div>
<div class="abs" style="left:820px;top:1290px;width:270px"><div class="svc-label" style="margin-left:183px">Date Night</div><div class="svc-desc right" style="margin-top:6px">Lorem ipsum dolor sit amet, consectetuer adipiscing elit</div></div>
<div class="abs" style="left:825px;top:1518px;width:270px"><div class="svc-label right">Parties</div><div class="svc-desc right" style="margin-top:6px">Lorem ipsum dolor sit amet, consectetuer adipiscing elit</div></div>
<div class="abs svc-active" style="left:108px;top:1200px"><div class="svc-label">Puzzles</div><div class="svc-desc" style="margin-top:6px">Lorem ipsum dolor sit amet, consectetuer adipiscing elit</div></div>
<div class="abs" style="left:110px;top:1385px"><div class="svc-label">Riddles</div><div class="svc-desc" style="margin-top:6px">Lorem ipsum dolor sit amet, consectetuer adipiscing elit</div></div>
<div class="abs" style="left:194px;top:1555px"><div class="svc-label">Mysteries</div><div class="svc-desc" style="margin-top:6px">Lorem ipsum dolor sit amet, consectetuer adipiscing elit</div></div>

<!-- gallery -->
<section class="abs gallery"></section>
<h2 class="abs gallery-title">Photo Gallery</h2>
<div class="abs gallery-rule"></div>
<svg class="abs" style="left:38px;top:1862px" width="30" height="52" viewBox="0 0 30 52"><path d="M28 2L3 26l25 24" stroke="#333" stroke-width="2" fill="none"/></svg>
<svg class="abs" style="left:1132px;top:1862px" width="30" height="52" viewBox="0 0 30 52"><path d="M2 2l25 24L2 50" stroke="#333" stroke-width="2" fill="none"/></svg>
<div class="abs photo" style="left:99px;background:linear-gradient(120deg,#2a2a2a,#8a8a8a 55%,#d0d0d0 75%,#3a3a3a)" role="img" aria-label="Black and white photo of a player shining a flashlight in a dark room"></div>
<div class="abs photo" style="left:453px;background:linear-gradient(120deg,#1d1d1b,#3a3a36 50%,#5e5e58)" role="img" aria-label="Photo of a dark wall covered in chalk letters and numbers"></div>
<div class="abs photo" style="left:805px;background:linear-gradient(120deg,#3b2f22,#8a7660 50%,#c9b7a0)" role="img" aria-label="Photo of two players searching a room with a barred cell"></div>
<p class="abs caption" style="left:99px">Lorem ipsum dolor sit amet, consectetuer</p>
<p class="abs caption" style="left:453px">Lorem ipsum dolor sit amet, consectetuer</p>
<p class="abs caption" style="left:805px">Lorem ipsum dolor sit amet, consectetuer</p>

<!-- footer -->
<footer class="abs footer"></footer>
<h3 class="abs foot-head" style="left:81px;font-weight:400">Quick Links</h3>
<ul class="abs foot-list">
  <li>Home</li><li>About Us</li><li>Services</li><li>Gallery</li><li>Contact Us</li>
</ul>
<div class="abs foot-sep" style="left:221px"></div>
<h3 class="abs foot-head" style="left:244px;font-weight:400">Contact Us</h3>
<div class="abs foot-row" style="left:246px;top:2145px">
  <svg width="11" height="15" viewBox="0 0 12 16"><path d="M6 0a6 6 0 0 1 6 6c0 4-6 10-6 10S0 10 0 6a6 6 0 0 1 6-6z" fill="#fff"/><circle cx="6" cy="6" r="2.2" fill="#333"/></svg>
  <span>4410 Linden Avenue Suite<br>12, Marlow TX</span>
</div>
<div class="abs foot-row" style="left:246px;top:2201px">
  <svg width="13" height="13" viewBox="0 0 24 24"><path d="M6.6 10.8a15 15 0 0 0 6.6 6.6l2.2-2.2a1 1 0 0 1 1-.25 11.4 11.4 0 0 0 3.6.57 1 1 0 0 1 1 1V20a1 1 0 0 1-1 1A17 17 0 0 1 3 4a1 1 0 0 1 1-1h3.5a1 1 0 0 1 1 1c0 1.25.2 2.45.57 3.57a1 1 0 0 1-.25 1z" fill="#fff"/></svg>
  <span>(555) 014-2290</span>
</div>
<div class="abs foot-row" style="left:246px;top:2243px">
  <svg width="13" height="10" viewBox="0 0 18 13"><rect width="18" height="13" fill="#fff"/><path d="M1 1l8 6 8-6" stroke="#333" stroke-width="1.5" fill="none"/></svg>
  <span>info@thelockhall.com</span>
</div>
<div class="abs foot-sep" style="left:459px"></div>
<div class="abs map" role="img" aria-label="Street map showing the location of the escape rooms"></div>
<div class="abs foot-sep" style="left:752px"></div>
<h3 class="abs foot-head" style="left:777px;font-weight:400">Get Social</h3>
<div class="abs foot-row" style="left:777px;top:2148px;align-items:center"><span class="social-dot"></span><span>Like Us</span></div>
<div class="abs foot-row" style="left:777px;top:2189px;align-items:center"><span class="social-dot"></span><span>Follow Us</span></div>
<div class="abs foot-row" style="left:777px;top:2230px;align-items:center"><span class="social-dot"></span><span>Follow Us</span></div>
<div class="abs foot-sep" style="left:909px"></div>
<div class="abs foot-brand">The Lock<br>Hall</div>
<div class="abs copyright">Copyright&nbsp; 2016 - The Lock Hall &nbsp;|&nbsp; All Rights Reserved</div>

</body>
</html>
```